Business Card Design Project

I need a business card for an environmentally friendly interior design company called Roomcraft Willow.
I was thinking it might be nice to print the business cards on brown recycled paper with green ink.
In addition to interior design, I will also be able to consult with homeowners regarding their indoor environments and how they might be affecting their health after May 2013 which is when I will complete my certification program. This can be added to the business card at that time: "Certified Habitat Vitalis Dwelling Consultant".
Health

```html
<!DOCTYPE html>
<html lang="en">
<head>
<meta charset="utf-8">
<title>Roomcraft Willow – Business Card</title>
<link rel="stylesheet" href="https://fonts.googleapis.com/css2?family=Bodoni+Moda:opsz,wght@6..96,700&display=swap">
<style>
  :root {
    --kraft: #a57a43;
    --kraft-light: #ad8350;
    --kraft-dark: #987039;
    --leaf-green: #8cc85a;
    --ink: #111111;
  }
  html, body {
    margin: 0;
    padding: 0;
    width: 1200px;
    height: 686px;
    overflow: hidden;
  }
  .card {
    position: relative;
    width: 1200px;
    height: 686px;
    background:
      radial-gradient(ellipse at 50% 45%, var(--kraft-light) 0%, var(--kraft) 55%, var(--kraft-dark) 100%);
    font-family: "Bodoni Moda", "Times New Roman", serif;
    font-weight: 700;
  }
  .brand-name {
    position: absolute;
    left: 0;
    right: 0;
    top: 150px;
    margin: 0;
    text-align: center;
    color: var(--leaf-green);
    font-size: 118px;
    line-height: 1.05;
    font-weight: 700;
    letter-spacing: 1px;
  }
  .brand-name span {
    display: block;
  }
  .contact-phone {
    position: absolute;
    left: 526px;
    top: 462px;
    margin: 0;
    color: var(--ink);
    font-size: 30px;
    font-weight: 700;
    white-space: nowrap;
  }
</style>
</head>
<body>
  <main class="card">
    <h1 class="brand-name"><span>Roomcraft</span><span>Willow</span></h1>
    <p class="contact-phone">Phone: 555-214-0378</p>
  </main>
</body>
</html>
```